Banner Pop Up Opt In Form REDESIGNS - SLEEK BLACK LOOK

Please redesign banners attached.

I am looking for a very sleek look....I do not like this collage of images on these current designs. Please keep all content same but use images that pop.

I have an acccount at www.pixmorrow-example.com or you can use your own images.

I like black background for somereason because it looks very sleek....but these designs should pop , build trust and credibility and have easy opt in form....SLEEK AND MODERN LOOK is what im looking for....

Target Market(s)

Consumers on websites

Requirements
Must have
• Please redesign banners attached.

Nice to have

Should not have

```html
<!DOCTYPE html>
<html lang="en">
<head>
<meta charset="utf-8">
<title>Great Offer Opt-In Banner</title>
<link rel="stylesheet" href="https://fonts.googleapis.com/css2?family=Bebas+Neue&family=Roboto+Condensed:wght@400&family=Roboto:wght@400;700&display=swap">
<style>
  :root {
    --ink: #000000;
    --ink-soft: #0b0b0d;
    --offer-yellow: #f8e400;
    --white: #ffffff;
    --field-border: #dcdcdc;
    --field-focus: #7fb3e0;
    --label-grey: #666666;
    --button-top: #a9d5f3;
    --button-bottom: #5ea9de;
    --button-text: #1f3550;
  }
  html, body {
    margin: 0;
    padding: 0;
    overflow: hidden;
    background: var(--ink);
  }
  .banner {
    position: relative;
    width: 1200px;
    height: 675px;
    overflow: hidden;
    background: var(--ink);
  }
  .hero {
    position: absolute;
    left: 0;
    top: 0;
    width: 640px;
    height: 675px;
    background:
      linear-gradient(180deg, #2b3aa8 0%, #7a4fb0 30%, #e4836a 47%, #f2b36a 51%, #1c1f4a 58%, #2a2f78 78%, #0d0f26 100%);
  }
  .hero__fade {
    position: absolute;
    left: 0;
    top: 0;
    width: 640px;
    height: 675px;
    background:
      linear-gradient(90deg, rgba(0,0,0,0) 0%, rgba(0,0,0,0) 45%, rgba(0,0,0,0.75) 78%, var(--ink) 100%),
      linear-gradient(180deg, rgba(0,0,0,0.35) 0%, rgba(0,0,0,0) 30%, rgba(0,0,0,0) 70%, rgba(0,0,0,0.6) 100%);
  }
  .offer {
    position: absolute;
    left: 650px;
    width: 490px;
    margin: 0;
    text-align: center;
    white-space: nowrap;
    font-family: "Bebas Neue", sans-serif;
    font-weight: 400;
  }
  .offer__headline {
    top: 36px;
    font-size: 76px;
    line-height: 1;
    color: var(--offer-yellow);
    letter-spacing: -1px;
  }
  .offer__subline {
    top: 112px;
    font-size: 36px;
    line-height: 31px;
    color: var(--white);
    letter-spacing: -1.6px;
  }
  .offer__prize {
    top: 180px;
    font-size: 33px;
    line-height: 1;
    color: var(--offer-yellow);
    letter-spacing: -0.6px;
  }
  .optin {
    position: absolute;
    left: 686px;
    top: 236px;
    width: 298px;
    height: 276px;
    margin: 0;
    background: var(--white);
    box-sizing: border-box;
    padding: 24px 22px 0;
    border-radius: 3px;
    font-family: "Roboto", sans-serif;
  }
  .optin__label {
    display: block;
    font-size: 9px;
    color: var(--label-grey);
    margin-bottom: 6px;
  }
  .optin__field {
    display: block;
    width: 254px;
    height: 35px;
    box-sizing: border-box;
    border: 1px solid var(--field-border);
    border-radius: 2px;
    margin-bottom: 20px;
  }
  .optin__field--active {
    border-color: var(--field-focus);
  }
  .optin__submit {
    display: block;
    margin: -9px auto 0;
    width: 90px;
    height: 34px;
    border: 1px solid #5b9fd0;
    border-radius: 2px;
    background: linear-gradient(180deg, var(--button-top), var(--button-bottom));
    color: var(--button-text);
    font-family: "Roboto", sans-serif;
    font-weight: 700;
    font-size: 12px;
  }
  .offer__note {
    position: absolute;
    left: 607px;
    top: 530px;
    margin: 0;
    white-space: nowrap;
    font-family: "Roboto Condensed", sans-serif;
    font-size: 19px;
    line-height: 23px;
    letter-spacing: -0.3px;
    color: var(--white);
  }
</style>
</head>
<body>
<div class="banner">
  <div class="hero" role="img" aria-label="Waterfront resort city skyline at dusk reflected in the bay"></div>
  <div class="hero__fade"></div>

  <h1 class="offer offer__headline">WANT A GREAT OFFER ?</h1>
  <p class="offer offer__subline">SUBSCRIBE TO OUR NEWSLETTER<br>TO ENTER TO WIN A</p>
  <p class="offer offer__prize">7 NIGHT RESORT / CONDO - 3500+ LOCATIONS</p>

  <form class="optin">
    <label class="optin__label" for="optin-name">Name</label>
    <input class="optin__field" id="optin-name" type="text">
    <label class="optin__label" for="optin-email">Email</label>
    <input class="optin__field" id="optin-email" type="email">
    <label class="optin__label" for="optin-phone">Phone</label>
    <input class="optin__field optin__field--active" id="optin-phone" type="tel">
    <button class="optin__submit" type="button">SUBMIT</button>
  </form>

  <p class="offer__note">We will send an email and a text message win<br>the offer and instructions on how to redeem.</p>
</div>
</body>
</html>
```